Need a powerful, eye-catching book cover design for a Public Relations book for Lawyers.

We need a beautiful, elegant, and professional cover for a public relations book. We’ll be selling this both to (1) creative, experienced legal marketers, and (2) conservative lawyers. It must grab their attention visually, and have a bold, easy to read headline. The cover image may wrap around to the back cover.SIZE: 6 x 9” 100 pagesTITLE: The Ultimate Public Relations Handbook for LawyersSUBHEAD: Make millions using media and the InternetCO-AUTHORSRoss Fishman, JDJohn HellermanInclude a CALLOUT quote: “The definitive PR book. Simple and powerful.” – Hal Brisket, SkaddenGRAPHICS:You may use one of the attached photos, crop or flip them however you’d like, or use something else entirely. DESCRIPTION for the back cover:Why do some law firms have the best reputations or command the highest hourly rates? Why are some the go-to firms or thought leaders in particular specialties? Why are your competitors in the media more than you? Two words: Public relations. The co-authors are known worldwide as leaders in public relations, legal marketing, and branding. Mark Tolliver is called, “A PR Guru.” Bar Ledger magazine wrote ““Many people consider Dale Warbeck to be the nation’s foremost expert on law firm marketing.”Hal Brisket built Valmont into the first firm to generate $1 billion in revenue. Nadine Cortez is the nation’s go-to lawyer for women’s issues. Your home town’s top PI lawyer gets the first look at the biggest cases. Why? Strategic, intentional, effective PR. Are you tired of toiling in anonymity? Want to earn the attention of reporters and editors who can build your credentials and reputation for expertise? Wouldn’t it be nice to have more clients begging you to represent them because they heard you were the best in town? That is what public relations is designed to do. Want to get more respect, earn more clients, and charge higher rates? Get known as a thought leader in a specialty practice or industry? Public relations could be your most-important marketing tool. And this book will teach you precisely how. Ready to catapult your practice to new heights? Take a deep breath and dive in….

Target Market(s)

1. Creative marketing professionals
2. Conservative 40-year-old lawyers

Industry/Entity Type

Legal

Font styles to use
Serif

Requirements
Must have
• Want a simple, bold, eye catching design conveying professionalism and quality. This is a practical, how-to book. We need a simple design and strong headline that will work well at a small thumbnail size on Quiverly.
Nice to have
• Perhaps the microphone could wrap around the cover? A tight crop of a microphone that creates an abstract could work. Let's create something memorable.

```html
<!DOCTYPE html>
<html lang="en">
<head>
<meta charset="utf-8">
<title>The Complete Press Outreach Guidebook for Attorneys – Cover Spread</title>
<link rel="stylesheet" href="https://fonts.googleapis.com/css2?family=Rubik:wght@500;600&family=Roboto+Slab:wght@400;700&family=Noto+Serif:ital,wght@0,400;0,700;1,400;1,700&display=swap">
<style>
  :root {
    --bg: #6b88c8;
    --paper: #ffffff;
    --navy: #1b2340;
    --red: #b51d2e;
    --body: #3a3f52;
    --wave-light: #f4f4f5;
    --wave-mid: #d9dadd;
    --mic-dark: #1e1f22;
    --mic-mid: #8c8e93;
  }
  * { box-sizing: border-box; margin: 0; padding: 0; }
  html, body { width: 862px; height: 1200px; overflow: hidden; }
  body { background: var(--bg); position: relative; font-family: "Noto Serif", serif; }

  .spread {
    position: absolute; left: 90px; top: 74px; width: 682px; height: 498px;
    background: var(--paper); overflow: hidden;
  }
  .waves {
    position: absolute; left: 0; bottom: 0; width: 100%; height: 140px;
  }
  .microphone {
    position: absolute; left: 374px; top: 254px; width: 64px; height: 244px;
  }

  /* back cover */
  .back-questions {
    position: absolute; left: 36px; top: 70px; width: 124px;
    font-size: 7.4px; line-height: 1.25; color: var(--navy);
  }
  .back-questions strong { font-weight: 700; }
  .back-hook { position: absolute; left: 177px; top: 71px; width: 130px; }
  .back-hook .lead {
    font-family: "Roboto Slab", serif; font-size: 8px; color: var(--red); margin-bottom: 4px;
  }
  .back-hook .headline {
    font-family: "Roboto Slab", serif; font-weight: 700; font-size: 28px;
    line-height: 1.05; color: var(--red);
  }
  .back-rule {
    position: absolute; left: 294px; top: 6px; width: 2px; height: 95px; background: var(--mic-dark);
  }
  .back-copy {
    position: absolute; top: 178px; width: 124px;
    font-size: 6.4px; line-height: 1.38; color: var(--body); text-align: justify;
  }
  .back-copy.col-one { left: 36px; }
  .back-copy.col-two { left: 177px; }
  .back-copy .sign-off {
    display: block; margin-top: 7px; font-style: italic; font-weight: 700; color: var(--navy);
  }

  /* spine */
  .spine-title, .spine-authors {
    position: absolute; writing-mode: vertical-rl; font-family: "Rubik", sans-serif; font-weight: 600;
    white-space: nowrap;
  }
  .spine-title { left: 334px; top: 38px; font-size: 8.6px; color: var(--red); letter-spacing: 0.1px; }
  .spine-authors { left: 335px; top: 350px; font-size: 6.2px; color: var(--navy); }

  /* front cover */
  .callout {
    position: absolute; left: 400px; top: 35px; width: 235px; text-align: center;
    font-size: 7.6px; line-height: 1.6; color: var(--navy);
  }
  .callout .quote { font-style: italic; }
  .callout .source strong { font-weight: 700; }
  .front-title {
    position: absolute; right: 37px; top: 90px; text-align: right;
    font-family: "Rubik", sans-serif; font-weight: 600; line-height: 1;
  }
  .front-title span { display: block; }
  .front-title .small-line { font-size: 25px; color: var(--navy); }
  .front-title .big-line { font-size: 47px; color: var(--red); margin-top: 4px; letter-spacing: -0.3px; }
  .front-title .tiny-line { font-size: 14px; color: var(--navy); margin-top: 6px; }
  .front-title .mid-line { font-size: 25px; color: var(--navy); margin-top: 3px; }
  .front-rule {
    position: absolute; left: 474px; top: 291px; width: 171px; height: 1.5px; background: var(--navy);
  }
  .subhead {
    position: absolute; right: 37px; top: 302px; text-align: right;
    font-family: "Roboto Slab", serif; font-size: 15.5px; line-height: 1.2; color: var(--navy);
  }
  .authors {
    position: absolute; right: 34px; top: 420px; text-align: right;
    font-family: "Rubik", sans-serif; font-weight: 600; font-size: 17px; line-height: 1.6; color: var(--navy);
  }
</style>
</head>
<body>
  <section class="spread" aria-label="Book cover wrap: back cover, spine and front cover">
    <svg class="waves" role="img" aria-label="Flowing grey wave-line pattern along the bottom of the wrap" viewBox="0 0 682 140" preserveAspectRatio="none">
      <defs>
        <linearGradient id="waveFill" x1="0" y1="0" x2="0" y2="1">
          <stop offset="0" stop-color="var(--paper)"/>
          <stop offset="0.45" stop-color="var(--wave-mid)"/>
          <stop offset="1" stop-color="var(--wave-light)"/>
        </linearGradient>
      </defs>
      <rect width="682" height="140" fill="url(#waveFill)"/>
    </svg>

    <!-- back cover -->
    <p class="back-questions">
      Why do some law firms have the <strong>best reputations</strong> or command the highest hourly rates?<br>
      Why are some the go-to firms or thought leaders in <strong>particular specialties?</strong><br>
      Why are your competitors in the media <strong>more than you?</strong>
    </p>
    <div class="back-hook">
      <p class="lead">Two words:</p>
      <p class="headline">Public<br>relations.</p>
    </div>
    <div class="back-rule"></div>
    <p class="back-copy col-one">The co-authors are known worldwide as leaders in public relations, legal marketing, and branding. Mark Tolliver is called, “A PR Guru.” Bar Ledger magazine wrote ““Many people consider Dale Warbeck to be the nation’s foremost expert on law firm marketing.”Hal Brisket built Valmont into the first firm to generate $1 billion in revenue. Nadine Cortez is the nation’s go-to lawyer for women’s issues. Your home town’s top PI lawyer gets the first look at the biggest cases. Why? Strategic, intentional, effective PR. Are you tired of toiling in anonymity? Want to earn the attention of reporters and editors who can build your credentials and reputation for expertise?</p>
    <p class="back-copy col-two">Wouldn’t it be nice to have more clients begging you to represent them because they heard you were the best in town? That is what public relations is designed to do. Want to get more respect, earn more clients, and charge higher rates? Get known as a thought leader in a specialty practice or industry? Public relations could be your most-important marketing tool. And this book will teach you precisely how. Ready to catapult your practice to new heights?
      <span class="sign-off">Take a deep breath and dive in….</span></p>

    <!-- spine -->
    <p class="spine-title">THE COMPLETE PRESS OUTREACH GUIDEBOOK FOR ATTORNEYS</p>
    <p class="spine-authors">DALE WARBECK &amp; JD MARK TOLLIVER</p>

    <!-- front cover -->
    <div class="microphone" role="img" aria-label="Photo of a chrome studio microphone on a black stand, rising from the bottom edge" style="background: linear-gradient(180deg, var(--mic-mid) 0%, #b9bbbf 22%, var(--mic-dark) 40%, var(--mic-dark) 100%); border-radius: 32px 32px 4px 4px;"></div>

    <div class="callout">
      <p class="quote">“The definitive PR book. Simple and powerful.”</p>
      <p class="source">- <strong>Hal Brisket</strong>, Valmont</p>
    </div>
    <h1 class="front-title">
      <span class="small-line">THE COMPLETE</span>
      <span class="big-line">PRESS</span>
      <span class="big-line">OUTREACH</span>
      <span class="tiny-line">GUIDEBOOK</span>
      <span class="mid-line">FOR ATTORNEYS</span>
    </h1>
    <div class="front-rule"></div>
    <p class="subhead">Make millions using<br>media and the Internet</p>
    <p class="authors">DALE WARBECK<br>JD MARK TOLLIVER</p>
  </section>
</body>
</html>
```